An international wholesale business needs letterhead design

Logo file is attached. Please design a letterhead with the following details:

- Company Name and Logo
- Address
- VAT Registration number
- Phone No
- Website address

```html
<!DOCTYPE html>
<html lang="en">
<head>
<meta charset="utf-8">
<title>Verano Trading Letterhead</title>
<link href="https://fonts.googleapis.com/css2?family=Open+Sans:wght@400;700&family=Poppins:wght@400;600&display=swap" rel="stylesheet">
<style>
  :root {
    --backdrop: #676767;
    --paper: #ffffff;
    --brand-red: #c1262f;
    --brand-grey: #8c9198;
    --ink: #2e2e2e;
    --muted: #8a8f96;
    --signature-tone: #efefef;
  }
  html, body {
    margin: 0;
    padding: 0;
    width: 893px;
    height: 1200px;
    overflow: hidden;
    background: var(--backdrop);
  }
  .stage {
    position: relative;
    width: 1240px;
    height: 1667px;
    transform: scale(0.72016);
    transform-origin: 0 0;
  }
  .letterhead {
    position: absolute;
    left: 93px;
    top: 88px;
    width: 1054px;
    height: 1490px;
    background: var(--paper);
    overflow: hidden;
    font-family: "Open Sans", Arial, sans-serif;
    color: var(--ink);
  }
  .brand {
    position: absolute;
    left: 100px;
    top: 56px;
    display: flex;
    align-items: center;
    gap: 12px;
  }
  .brand-dot {
    width: 72px;
    height: 72px;
    border-radius: 50%;
    background: var(--brand-red);
  }
  .brand-name {
    font-family: "Poppins", Arial, sans-serif;
    font-weight: 600;
    font-size: 28px;
    letter-spacing: 0.5px;
    color: var(--brand-red);
    white-space: nowrap;
  }
  .header-url {
    position: absolute;
    left: 736px;
    top: 80px;
    font-family: "Poppins", Arial, sans-serif;
    font-size: 20px;
    color: var(--muted);
  }
  .header-url .accent { color: var(--brand-red); }
  .rule-grey {
    position: absolute;
    left: 483px;
    top: 113px;
    width: 51px;
    height: 4px;
    background: var(--brand-grey);
  }
  .rule-red {
    position: absolute;
    left: 538px;
    top: 113px;
    width: 516px;
    height: 4px;
    background: var(--brand-red);
  }
  .recipient {
    position: absolute;
    left: 100px;
    top: 255px;
    font-size: 22px;
    line-height: 34px;
  }
  .recipient strong { font-weight: 700; }
  .body-copy {
    position: absolute;
    left: 100px;
    top: 485px;
    width: 850px;
    font-size: 22px;
    line-height: 35.5px;
  }
  .body-copy p { margin: 0 0 36px; }
  .signature-mark {
    position: absolute;
    left: 80px;
    top: 1032px;
    width: 240px;
    height: 108px;
    background: var(--signature-tone);
    border-radius: 6px;
  }
  .signatory {
    position: absolute;
    left: 100px;
    top: 1140px;
    font-size: 22px;
    line-height: 34px;
  }
  .signatory-name {
    font-weight: 700;
    font-size: 26px;
  }
  .footer-company {
    position: absolute;
    left: 363px;
    top: 1333px;
    font-family: "Poppins", Arial, sans-serif;
    font-size: 21px;
    line-height: 30px;
    color: var(--muted);
  }
  .footer-company strong { font-weight: 600; }
  .footer-contacts {
    position: absolute;
    left: 644px;
    top: 1333px;
    margin: 0;
    padding: 0;
    list-style: none;
    font-family: "Poppins", Arial, sans-serif;
    font-size: 21px;
    line-height: 30.5px;
    color: var(--muted);
  }
  .footer-contacts li {
    display: flex;
    align-items: center;
    gap: 9px;
  }
  .footer-contacts svg { flex: none; }
</style>
</head>
<body>
<div class="stage">
  <div class="letterhead">
    <div class="brand">
      <div class="brand-dot"></div>
      <div class="brand-name">VERANO TRADING</div>
    </div>
    <div class="header-url"><span class="accent">VERANO</span>TRADING.COM</div>
    <div class="rule-grey"></div>
    <div class="rule-red"></div>

    <div class="recipient">
      To<br>
      <strong>John Doe</strong><br>
      Company Name<br>
      Address, and City Name<br>
      8978 Country Name
    </div>

    <div class="body-copy">
      <p>Lorem ipsum dolor sit amet, consectetur adipiscing elit, sed do eiusmod tempor incididunt ut labore et dolore magna aliqua. Ut enim ad minim veniam, quis nostrud exercitation ullamco laboris nisi ut aliquip.</p>
      <p>Sed ut perspiciatis unde omnis iste natus error sit voluptatem accusantium doloremque laudantium, totam rem aperiam, eaque ipsa quae ab illo inventore veritatis et quasi architecto beatae vitae dicta sunt explicabo. Nemo enim ipsam voluptatem quia voluptas sit aspernatur aut odit aut fugit, sed quia consequun&shy;tur magni dolores eos qui ratione voluptatem sequi nesciunt.</p>
      <p>Neque porro quisquam est, qui dolorem ipsum quia dolor sit amet, consectetur, adipisci velit, sed quia non numquam eius modi tempora incidunt ut labore et dolore magnam aliquam quaerat voluptatem.</p>
    </div>

    <div class="signature-mark" role="img" aria-label="Handwritten signature of the manager"></div>
    <div class="signatory">
      <div class="signatory-name">Marcus Hale</div>
      <div>Manager</div>
    </div>

    <div class="footer-company">
      <strong>VERANO TRADING</strong><br>
      VAT Reg#: VT2048815
    </div>

    <ul class="footer-contacts">
      <li>
        <svg width="20" height="20" viewBox="0 0 20 20" aria-hidden="true">
          <circle cx="10" cy="10" r="10" fill="var(--brand-red)"/>
          <path d="M10 4.5a3.5 3.5 0 0 0-3.5 3.5c0 2.6 3.5 7 3.5 7s3.5-4.4 3.5-7A3.5 3.5 0 0 0 10 4.5z" fill="none" stroke="#fff" stroke-width="1.4"/>
          <circle cx="10" cy="8" r="1.2" fill="#fff"/>
        </svg>
        123 Put Address Here, Here
      </li>
      <li>
        <svg width="20" height="20" viewBox="0 0 20 20" aria-hidden="true">
          <circle cx="10" cy="10" r="10" fill="var(--brand-red)"/>
          <path d="M6.5 5.5l2 0 .8 2.4-1.2 1a6 6 0 0 0 3 3l1-1.2 2.4.8v2a1 1 0 0 1-1 1A8 8 0 0 1 5.5 6.5a1 1 0 0 1 1-1z" fill="none" stroke="#fff" stroke-width="1.3" stroke-linejoin="round"/>
        </svg>
        +988 555 01234
      </li>
      <li>
        <svg width="20" height="20" viewBox="0 0 20 20" aria-hidden="true">
          <circle cx="10" cy="10" r="10" fill="var(--brand-red)"/>
          <path d="M6 6l8 3-3.4 1.2L9.2 14z" fill="none" stroke="#fff" stroke-width="1.4" stroke-linejoin="round"/>
        </svg>
        www.VeranoTrading.com
      </li>
    </ul>
  </div>
</div>
</body>
</html>
```